Bellmont Planners, LLC Stationary

Bellmont Planners, LLC is a new financial planning and consulting company. We are looking for designs on business cards, letterhead, envelopes, and anything else that would be useful. Our preference for business card design is two sided. We are looking for a professional and clean look with incorporating the logo and patriotic feel. Thank you to all who participate and good luck!

```html
<!DOCTYPE html>
<html lang="en">
<head>
<meta charset="utf-8">
<title>Bellmont Planners, LLC Stationery</title>
<link rel="stylesheet" href="https://fonts.googleapis.com/css2?family=Montserrat:wght@700&family=Open+Sans:wght@400;600;700&display=swap">
<style>
  :root{
    --navy:#153f6b;
    --red:#c4202b;
    --paper:#ffffff;
    --backdrop:#d6d6d6;
    --ink:#153f6b;
  }
  *{box-sizing:border-box;margin:0;padding:0}
  html,body{width:1200px;height:1200px;overflow:hidden}
  body{background:var(--backdrop);position:relative;font-family:"Open Sans",sans-serif;color:var(--ink)}
  .sheet{position:absolute;background:var(--paper);overflow:hidden;box-shadow:0 6px 18px rgba(0,0,0,.18)}
  .sheet svg.wave{position:absolute;left:0;top:0;width:100%;height:100%}

  .brand{display:flex;align-items:center;gap:8px;font-family:"Montserrat",sans-serif;font-weight:700;color:var(--navy);letter-spacing:.04em;text-transform:uppercase;white-space:nowrap}
  .brand .dot{width:12px;height:12px;border-radius:50%;background:var(--navy);flex:none}
  .brand.on-navy{color:#fff}
  .brand.on-navy .dot{background:#fff}
  .tagline{font-family:"Montserrat",sans-serif;font-weight:700;font-size:7px;letter-spacing:.12em;text-transform:uppercase;color:var(--navy);white-space:nowrap}
  .tagline.on-navy{color:#fff;opacity:.85}

  /* business card back */
  .card-back{left:50px;top:50px;width:430px;height:246px;background:var(--navy);display:flex;flex-direction:column;align-items:center;justify-content:center;gap:6px}
  .card-back .brand{font-size:19px}

  /* business card front */
  .card-front{left:50px;top:330px;width:430px;height:246px}
  .card-front .brand{position:absolute;left:22px;top:18px;font-size:17px}
  .card-front .tagline{position:absolute;left:42px;top:42px}
  .person{position:absolute;left:22px;top:62px}
  .person .name{font-weight:700;font-size:12px;line-height:1.3;color:var(--red);text-transform:uppercase;letter-spacing:.03em}
  .person .role{font-size:9px;line-height:1.3;color:var(--navy);margin-bottom:4px}
  .contact-list{list-style:none;font-size:9px;line-height:1.4;color:var(--navy)}
  .contact-list li{display:flex;align-items:center;gap:5px}
  .contact-list .ico{width:7px;height:7px;border-radius:50%;background:var(--red);flex:none}

  /* envelope back */
  .envelope-back{left:620px;top:50px;width:500px;height:246px}
  .envelope-back .flap{position:absolute;left:0;top:0;width:100%;height:72px}
  .envelope-back .flap-content{position:absolute;left:0;top:0;width:100%;height:64px;display:flex;flex-direction:column;align-items:center;justify-content:center;gap:3px}
  .envelope-back .brand{font-size:13px}
  .envelope-back .brand .dot{width:9px;height:9px}
  .envelope-back .tagline{font-size:5px}

  /* envelope front */
  .envelope-front{left:620px;top:330px;width:500px;height:246px}
  .envelope-front .brand{position:absolute;left:24px;top:22px;font-size:18px}
  .envelope-front .tagline{position:absolute;left:44px;top:47px}
  .envelope-front .return-address{position:absolute;left:44px;top:62px;font-size:10px;font-weight:600;line-height:1.35;color:var(--navy)}
  .envelope-front .return-address .ico{display:inline-block;width:7px;height:7px;border-radius:50%;background:var(--red);margin-right:4px}

  /* letterhead */
  .letterhead{left:412px;top:620px;width:376px;height:532px}
  .letterhead .contact-list{position:absolute;right:22px;top:22px;font-size:6.5px;line-height:1.4}
  .letterhead .contact-list .ico{width:5px;height:5px}
  .letterhead .brand{position:absolute;left:22px;top:96px;font-size:14px}
  .letterhead .brand .dot{width:10px;height:10px}
  .letterhead .tagline{position:absolute;left:40px;top:117px;font-size:5.5px}
</style>
</head>
<body>

<section class="sheet card-back" aria-label="Business card, reverse side">
  <div class="brand on-navy"><span class="dot"></span>Bellmont Planners, LLC</div>
  <div class="tagline on-navy">Financial planning and consulting</div>
</section>

<section class="sheet card-front" aria-label="Business card, front side">
  <svg class="wave" viewBox="0 0 430 246" preserveAspectRatio="none" aria-hidden="true">
    <path fill="var(--red)" d="M0,184 C140,204 280,212 430,216 L430,222 C280,219 140,213 0,194 Z"/>
    <path fill="var(--red)" d="M0,202 C140,220 280,226 430,228 L430,237 C280,236 140,232 0,218 Z"/>
    <path fill="var(--navy)" d="M40,246 C180,238 310,240 430,242 L430,246 Z"/>
  </svg>
  <div class="brand"><span class="dot"></span>Bellmont Planners, LLC</div>
  <div class="tagline">Financial planning and consulting</div>
  <div class="person">
    <p class="name">Elena Marsh</p>
    <p class="role">Principal</p>
    <ul class="contact-list">
      <li><span class="ico"></span>0400 555 218</li>
      <li><span class="ico"></span>+61 7 3000 0147</li>
      <li><span class="ico"></span>elena@bellmontplanners.com</li>
      <li><span class="ico"></span>www.bellmontplanners.com</li>
      <li><span class="ico"></span>12 Harlow Street Norwood, Qld 4102 Brisbane</li>
    </ul>
  </div>
</section>

<section class="sheet envelope-back" aria-label="Envelope, back with flap">
  <svg class="flap" viewBox="0 0 500 72" preserveAspectRatio="none" aria-hidden="true">
    <path fill="var(--navy)" d="M0,0 H500 V64 L486,72 H0 Z"/>
  </svg>
  <div class="flap-content">
    <div class="brand on-navy"><span class="dot"></span>Bellmont Planners, LLC</div>
    <div class="tagline on-navy">Financial planning and consulting</div>
  </div>
</section>

<section class="sheet envelope-front" aria-label="Envelope, front">
  <svg class="wave" viewBox="0 0 500 246" preserveAspectRatio="none" aria-hidden="true">
    <path fill="var(--red)" d="M0,100 C150,168 320,190 500,196 L500,204 C320,200 150,182 0,116 Z"/>
    <path fill="var(--red)" d="M0,132 C160,196 330,210 500,212 L500,226 C330,226 160,218 0,168 Z"/>
    <path fill="var(--navy)" d="M120,246 C250,232 380,232 500,232 L500,246 Z"/>
  </svg>
  <div class="brand"><span class="dot"></span>Bellmont Planners, LLC</div>
  <div class="tagline">Financial planning and consulting</div>
  <p class="return-address"><span class="ico"></span>12 Harlow Street Norwood<br>Qld 4102 Brisbane</p>
</section>

<section class="sheet letterhead" aria-label="Letterhead">
  <svg class="wave" viewBox="0 0 376 532" preserveAspectRatio="none" aria-hidden="true">
    <path fill="var(--red)" d="M286,272 C298,400 220,482 110,532 L126,532 C236,482 312,400 298,272 Z"/>
    <path fill="var(--red)" d="M314,278 C328,410 262,490 170,532 L200,532 C290,490 346,410 332,284 Z"/>
    <path fill="var(--navy)" d="M346,290 C360,420 304,500 236,532 L376,532 L376,304 Z"/>
  </svg>
  <ul class="contact-list">
    <li><span class="ico"></span>0400 555 218</li>
    <li><span class="ico"></span>+61 7 3000 0147</li>
    <li><span class="ico"></span>elena@bellmontplanners.com</li>
    <li><span class="ico"></span>www.bellmontplanners.com</li>
    <li><span class="ico"></span>12 Harlow Street Norwood</li>
    <li><span class="ico"></span>Qld 4102 Brisbane</li>
  </ul>
  <div class="brand"><span class="dot"></span>Bellmont Planners, LLC</div>
  <div class="tagline">Financial planning and consulting</div>
</section>

</body>
</html>
```